Natural Cosmetics need a Packaging Design

We need a PACKAGING design for labels on hand/body wash bottles and soap paper boxes.
We target at high end markets.
We expect a contemporary and trendy design.
We don't need a separate logo. The brand name "Va Mirel" acts as the logo.
We want a modern and classic font for "Va Mirel".
Please see attached pictures for packaging samples.

Industry/Entity Type

Cosmetics

Requirements
Should not have
• a separate logo from the brand name

```html
<!DOCTYPE html>
<html lang="en">
<head>
<meta charset="utf-8">
<title>Va Mirel Soap Crafters – Soap Box Label</title>
<link rel="stylesheet" href="https://fonts.googleapis.com/css2?family=Poiret+One&family=Raleway:wght@300;400&display=swap">
<style>
  :root {
    --page-bg: #ffffff;
    --label-bg: #eee5ae;
    --panel-white: #ffffff;
    --panel-grey: #eef1f2;
    --ink-green: #2f3b2a;
    --ink-soft: #4a5346;
    --rule: #8c918a;
    --leaf-dark: #3f6b5c;
    --leaf-mid: #6f9a86;
    --leaf-light: #a9c2b2;
  }
  html, body {
    margin: 0;
    padding: 0;
    width: 1131px;
    height: 1200px;
    overflow: hidden;
    background: var(--page-bg);
  }
  .canvas {
    position: relative;
    width: 1131px;
    height: 1200px;
  }
  .soap-label {
    position: absolute;
    left: 236px;
    top: 308px;
    width: 633px;
    height: 522px;
    background: var(--label-bg);
    border-radius: 7px;
    overflow: hidden;
  }
  .info-panel {
    position: absolute;
    left: 0;
    top: 82px;
    width: 532px;
    height: 359px;
    background: linear-gradient(90deg, var(--panel-white) 0%, var(--panel-white) 40%, var(--panel-grey) 100%);
    border-radius: 0 4px 4px 0;
  }
  .brand-name {
    position: absolute;
    left: 24px;
    top: 38px;
    margin: 0;
    font-family: "Poiret One", sans-serif;
    font-weight: 400;
    font-size: 70px;
    line-height: 1;
    letter-spacing: 1px;
    color: var(--ink-green);
    white-space: nowrap;
  }
  .brand-trade {
    position: absolute;
    left: 25px;
    top: 124px;
    margin: 0;
    font-family: "Poiret One", sans-serif;
    font-size: 40px;
    line-height: 1;
    color: var(--ink-green);
    white-space: nowrap;
  }
  .divider {
    position: absolute;
    left: 26px;
    top: 185px;
    width: 284px;
    height: 1px;
    background: var(--rule);
  }
  .claim {
    position: absolute;
    left: 25px;
    top: 212px;
    margin: 0;
    font-family: "Poiret One", sans-serif;
    color: var(--ink-soft);
    line-height: 1;
  }
  .claim-main {
    display: block;
    font-size: 31px;
  }
  .claim-sub {
    display: block;
    margin-top: 8px;
    font-size: 24px;
    white-space: nowrap;
  }
  .tagline {
    position: absolute;
    left: 26px;
    top: 285px;
    margin: 0;
    font-family: "Raleway", sans-serif;
    font-weight: 300;
    font-size: 11px;
    color: var(--ink-soft);
  }
  .foliage {
    position: absolute;
    display: block;
  }
  .foliage-top {
    left: 0;
    top: 0;
    width: 420px;
    height: 110px;
  }
  .foliage-bottom {
    left: 288px;
    top: 250px;
    width: 345px;
    height: 272px;
  }
</style>
</head>
<body>
<main class="canvas">
  <section class="soap-label">
    <div class="info-panel">
      <h1 class="brand-name">VA MIREL</h1>
      <p class="brand-trade">SOAP CRAFTERS</p>
      <div class="divider"></div>
      <p class="claim">
        <span class="claim-main">ORGANIC</span>
        <span class="claim-sub">FOOD FOR HEALTHY SKINY</span>
      </p>
      <p class="tagline">Simple luxuries for bath and body</p>
    </div>

    <svg class="foliage foliage-top" viewBox="0 0 420 110" role="img" aria-label="Watercolour illustration of green leafy branches across the top left corner">
      <defs>
        <radialGradient id="leafGlowTop" cx="45%" cy="35%" r="60%">
          <stop offset="0%" stop-color="var(--leaf-mid)" stop-opacity="0.75"/>
          <stop offset="60%" stop-color="var(--leaf-light)" stop-opacity="0.45"/>
          <stop offset="100%" stop-color="var(--leaf-light)" stop-opacity="0"/>
        </radialGradient>
      </defs>
      <ellipse cx="190" cy="45" rx="230" ry="70" fill="url(#leafGlowTop)"/>
    </svg>

    <svg class="foliage foliage-bottom" viewBox="0 0 345 272" role="img" aria-label="Watercolour illustration of green leafy branches in the bottom right corner">
      <defs>
        <radialGradient id="leafGlowBottom" cx="70%" cy="70%" r="65%">
          <stop offset="0%" stop-color="var(--leaf-dark)" stop-opacity="0.7"/>
          <stop offset="55%" stop-color="var(--leaf-mid)" stop-opacity="0.4"/>
          <stop offset="100%" stop-color="var(--leaf-light)" stop-opacity="0"/>
        </radialGradient>
      </defs>
      <ellipse cx="230" cy="190" rx="200" ry="150" fill="url(#leafGlowBottom)"/>
    </svg>
  </section>
</main>
</body>
</html>
```